Kinsmen Crest Beard Oil Label for 1oz dropper bottle

Create a label for a 1oz beard oil dropper bottle. The label is 1.5 inches tall and 2.75 inches wide. Our logo is listed in the brief so please use it but it doesnt have to be that prominent. BEARD OIL is the most important verbiage. We like elements of all the attached images but we want our own look and feel.

Target Market(s)

Men with beards

Requirements
Must have
• Kinsmen Crest Logo, BEARD OIL, Flavor (Tobacco Vanilla)

Ingredients
Fractionated Coconut Oil (MCT)
Golden Jojoba Oil
Hemp Seed Oil
Tea Tree Essential Oil
Orange Bitter Essential Oil
Peppermint Supreme Essential Oil
Tallow Aromas
DYE FREE

Directions:
Directions: apply 3-6 drops into your hand...rub oil into hands and apply directly onto beard. For best results massage into skin under beard area and work oil out towards beard. Discontinue use if skin becomes irritated.

100% MADE IN THE USA (American Flag 1 color)
Veteran Owned Co.
Nice to have
• Labels can change color with each flavor or a ring can change color to show flavor.

```html
<!DOCTYPE html>
<html lang="en">
<head>
<meta charset="utf-8">
<title>Kinsmen Crest Beard Oil Label</title>
<link rel="stylesheet" href="https://fonts.googleapis.com/css2?family=Bebas+Neue&family=Courier+Prime:wght@700&family=Old+Standard+TT:wght@400;700&family=Oswald:wght@400&family=Rye&display=swap">
<style>
  :root {
    --paper: #ffffff;
    --ink: #111111;
    --label-bg: #161616;
    --label-bg-edge: #0c0c0c;
    --label-text: #f2f2f2;
    --accent-red: #c4262c;
    --shadow-grey: #3b3b3b;
    --ornament: #9a9a9a;
  }
  * { margin: 0; padding: 0; box-sizing: border-box; }
  html, body { width: 700px; height: 1200px; overflow: hidden; background: var(--paper); }
  .canvas { position: relative; width: 700px; height: 1200px; }

  .brand-mark {
    position: absolute; top: 62px; left: 0; width: 700px;
    text-align: center;
    font-family: "Bebas Neue", sans-serif;
    font-size: 86px; line-height: 1; letter-spacing: 2px;
    color: var(--ink);
  }

  .label {
    position: absolute; left: 30px; top: 814px;
    width: 642px; height: 352px;
    background: radial-gradient(ellipse at center, var(--label-bg) 60%, var(--label-bg-edge) 100%);
    color: var(--label-text);
    overflow: hidden;
  }

  .ingredients {
    position: absolute; left: 16px; top: 34px; width: 130px;
    font-family: "Old Standard TT", serif;
    font-size: 12.5px; line-height: 15.6px;
  }
  .ingredients h2 {
    font-family: "Old Standard TT", serif;
    font-weight: 700; font-size: 15px; line-height: 18px;
    color: var(--accent-red);
  }
  .ingredients ul { list-style: none; }

  .badge {
    position: absolute; top: 269px; width: 48px; height: 48px;
    border-radius: 50%; border: 2px solid var(--label-text);
    background: var(--label-bg);
  }
  .badge-usa { left: 16px; }
  .badge-veteran { left: 71px; }

  .rule { position: absolute; top: 30px; width: 12px; height: 300px; }
  .rule-left-a { left: 140px; }
  .rule-left-b { left: 168px; }
  .rule-right-a { left: 477px; }
  .rule-right-b { left: 508px; }

  .side-motto {
    position: absolute; top: 30px; height: 300px;
    writing-mode: vertical-rl; text-orientation: mixed;
    font-family: "Courier Prime", monospace; font-weight: 700;
    font-size: 13px; letter-spacing: 3.2px; text-align: center;
  }
  .motto-left { left: 150px; width: 18px; }
  .motto-right { left: 487px; width: 20px; }

  .front {
    position: absolute; left: 190px; top: 0; width: 290px; height: 352px;
    text-align: center;
  }
  .front-brand {
    position: absolute; top: 60px; left: 0; width: 100%;
    font-family: "Bebas Neue", sans-serif; font-size: 42px; line-height: 1;
    color: var(--label-text);
  }
  .front-claim {
    position: absolute; top: 124px; left: 0; width: 100%;
    font-family: "Rye", serif; font-size: 15px; letter-spacing: 0.5px;
  }
  .product-name {
    position: absolute; top: 138px; left: 0; width: 100%;
    font-family: "Bebas Neue", sans-serif; font-size: 98px; line-height: 1;
    color: var(--accent-red);
    text-shadow: 3px 3px 0 var(--shadow-grey);
  }
  .flourish {
    position: absolute; top: 236px; left: 40px; width: 210px; height: 14px;
    background: linear-gradient(90deg, transparent, var(--ornament) 20%, var(--ornament) 80%, transparent);
    opacity: 0.35; border-radius: 7px;
  }
  .flavor {
    position: absolute; top: 266px; left: 20px; width: 250px; height: 30px;
  }
  .flavor-name {
    position: absolute; top: 0; left: 30px; width: 190px; height: 30px;
    font-family: "Old Standard TT", serif; font-size: 16px; line-height: 30px;
    color: var(--accent-red); letter-spacing: 0.3px;
  }
  .volume {
    position: absolute; top: 312px; left: 0; width: 100%;
    font-family: "Oswald", sans-serif; font-size: 16px; letter-spacing: 0.3px;
  }

  .directions {
    position: absolute; left: 528px; top: 32px; width: 100px; height: 296px;
  }
  .directions-text {
    position: absolute; top: 0; left: 0; width: 296px; height: 100px;
    transform-origin: top left;
    transform: translateY(296px) rotate(-90deg);
    font-family: "Old Standard TT", serif; font-size: 11.2px; line-height: 16.6px;
  }
  .directions-text h2 {
    font-size: 15px; line-height: 17px; font-weight: 700; color: var(--accent-red);
  }
</style>
</head>
<body>
<main class="canvas">
  <div class="brand-mark">Kinsmen Crest</div>

  <section class="label" aria-label="Kinsmen Crest beard oil label">
    <div class="ingredients">
      <h2>Ingredients</h2>
      <ul>
        <li>Fractionated</li>
        <li>Coconut Oil (MCT)</li>
        <li>Golden Jojoba Oil</li>
        <li>Hemp Seed Oil</li>
        <li>Tea Tree</li>
        <li>Essential Oil</li>
        <li>Orange Bitter</li>
        <li>Essential Oil</li>
        <li>Peppermint</li>
        <li>Supreme</li>
        <li>Essential Oil</li>
        <li>Tallow Aromas</li>
        <li>DYE FREE</li>
      </ul>
    </div>
    <div class="badge badge-usa" role="img" aria-label="Made in USA badge"></div>
    <div class="badge badge-veteran" role="img" aria-label="Veteran owned badge"></div>

    <svg class="rule rule-left-a" viewBox="0 0 12 300" aria-hidden="true"><line x1="6" y1="4" x2="6" y2="296" stroke="#f2f2f2" stroke-width="1.2"/><path d="M6 0 L9 5 L6 10 L3 5Z M6 290 L9 295 L6 300 L3 295Z" fill="#f2f2f2"/><circle cx="6" cy="150" r="4" fill="#f2f2f2"/></svg>
    <div class="side-motto motto-left">BOTTLED BY A BEARDED MAN</div>
    <svg class="rule rule-left-b" viewBox="0 0 12 300" aria-hidden="true"><line x1="6" y1="4" x2="6" y2="296" stroke="#f2f2f2" stroke-width="1.2"/><path d="M6 0 L9 5 L6 10 L3 5Z M6 290 L9 295 L6 300 L3 295Z" fill="#f2f2f2"/><circle cx="6" cy="150" r="4" fill="#f2f2f2"/></svg>

    <div class="front">
      <div class="front-brand">Kinsmen Crest</div>
      <div class="front-claim">100% PURE ORGANIC</div>
      <h1 class="product-name">BEARDOIL</h1>
      <div class="flourish" role="img" aria-label="Decorative scroll flourish"></div>
      <div class="flavor">
        <svg width="250" height="30" viewBox="0 0 250 30" aria-hidden="true">
          <line x1="0" y1="15" x2="28" y2="15" stroke="#f2f2f2" stroke-width="1.5" stroke-dasharray="2 2"/>
          <line x1="222" y1="15" x2="250" y2="15" stroke="#f2f2f2" stroke-width="1.5" stroke-dasharray="2 2"/>
          <path d="M42 1 H208 L222 15 L208 29 H42 L28 15 Z" fill="#ffffff"/>
          <path d="M45 4 H205 L216 15 L205 26 H45 L34 15 Z" fill="none" stroke="#c4262c" stroke-width="0.8"/>
        </svg>
        <div class="flavor-name">TOBACCOVANILLA</div>
      </div>
      <div class="volume">30ML/1FL.OZ</div>
    </div>

    <svg class="rule rule-right-a" viewBox="0 0 12 300" aria-hidden="true"><line x1="6" y1="4" x2="6" y2="296" stroke="#f2f2f2" stroke-width="1.2"/><path d="M6 0 L9 5 L6 10 L3 5Z M6 290 L9 295 L6 300 L3 295Z" fill="#f2f2f2"/><circle cx="6" cy="150" r="4" fill="#f2f2f2"/></svg>
    <div class="side-motto motto-right">QUALITY &amp; CRAFTSMANSHIP</div>
    <svg class="rule rule-right-b" viewBox="0 0 12 300" aria-hidden="true"><line x1="6" y1="4" x2="6" y2="296" stroke="#f2f2f2" stroke-width="1.2"/><path d="M6 0 L9 5 L6 10 L3 5Z M6 290 L9 295 L6 300 L3 295Z" fill="#f2f2f2"/><circle cx="6" cy="150" r="4" fill="#f2f2f2"/></svg>

    <div class="directions">
      <div class="directions-text">
        <h2>Directions:</h2>
        <p>Directions: apply 3-6 drops into your hand...rub oil into hands and apply directly onto beard. For best results massage into skin under beard area and work oil out towards beard. Discontinue use if skin becomes irritated.</p>
      </div>
    </div>
  </section>
</main>
</body>
</html>
```